Business Card Design Project

We need a business card design for a new construction company called 'KORVA HOLDINGS PTY.LTD' We run a construction based company for high end market homes in melbourne, we want something that looks professional and eye catching.The card needs to have a strong design to it something modern as the company name explains "korva." The final design should communicate professionalism and a strong image to our customers on the quality of our work.
On the business card i need
Name: Marek Holtvay
Mob:0417295031
Email:korva.holdings@mailbrook.example
Domestic/Residential/Commercial

```html
<!DOCTYPE html>
<html lang="en">
<head>
<meta charset="utf-8">
<title>Korva Holdings – Business Card</title>
<link href="https://fonts.googleapis.com/css2?family=Questrial&display=swap" rel="stylesheet">
<style>
  :root {
    --page: #ffffff;
    --card-dark: #1d1d1e;
    --card-dark-edge: #151516;
    --brand-red: #7c1b16;
    --brand-red-deep: #6a1612;
    --ink-light: #f4f1ee;
    --ink-soft: rgba(244, 241, 238, 0.82);
    --ghost: rgba(255, 255, 255, 0.07);
    --ghost-red: rgba(0, 0, 0, 0.14);
  }
  * { margin: 0; padding: 0; box-sizing: border-box; }
  html, body {
    width: 1100px;
    height: 1200px;
    overflow: hidden;
    background: var(--page);
  }
  body {
    position: relative;
    font-family: "Questrial", "Century Gothic", sans-serif;
  }
  .card {
    position: absolute;
    left: 53px;
    width: 1000px;
    height: 572px;
    overflow: hidden;
    background:
      radial-gradient(ellipse at 60% 40%, #232324 0%, var(--card-dark) 60%, var(--card-dark-edge) 100%);
  }
  .card--front { top: 24px; }
  .card--back { top: 614px; }

  .card__band {
    position: absolute;
    left: 60px;
    top: 0;
    width: 334px;
    height: 100%;
    background: linear-gradient(180deg, var(--brand-red) 0%, var(--brand-red-deep) 100%);
  }
  .card__band-block {
    position: absolute;
    left: 32px;
    top: 300px;
    width: 270px;
    height: 272px;
    background: var(--ghost-red);
  }

  .brand {
    position: absolute;
    left: 76px;
    top: 54px;
    color: var(--ink-light);
  }
  .brand__name {
    display: block;
    font-size: 92px;
    line-height: 1;
    letter-spacing: 2px;
  }
  .brand__legal {
    display: block;
    margin-top: 4px;
    font-size: 13px;
    letter-spacing: 6.2px;
  }
  .brand__services {
    display: block;
    margin-top: 18px;
    font-size: 14px;
    letter-spacing: 1px;
    color: var(--ink-soft);
  }

  .ghost-brand {
    position: absolute;
    left: 404px;
    top: 170px;
    color: var(--ghost);
  }
  .ghost-brand__name {
    display: block;
    font-size: 170px;
    line-height: 1;
    letter-spacing: 22px;
  }
  .ghost-brand__legal {
    display: block;
    margin-top: 10px;
    font-size: 26px;
    letter-spacing: 16px;
  }

  .contact {
    position: absolute;
    left: 580px;
    top: 450px;
    color: var(--ink-light);
  }
  .contact__name {
    font-size: 31px;
    line-height: 1.2;
    margin-bottom: 6px;
  }
  .contact__line {
    font-size: 21px;
    line-height: 1.35;
  }
</style>
</head>
<body>

  <section class="card card--front">
    <div class="card__band">
      <div class="card__band-block"></div>
    </div>
    <div class="ghost-brand" aria-hidden="true">
      <span class="ghost-brand__name">korva</span>
      <span class="ghost-brand__legal">HOLDINGS PTY.LTD</span>
    </div>
    <div class="brand">
      <span class="brand__name">korva</span>
      <span class="brand__legal">KORVA HOLDINGS PTY.LTD</span>
      <span class="brand__services">Domestic / Residential / Commercial</span>
    </div>
    <div class="contact">
      <p class="contact__name">Marek Holtvay</p>
      <p class="contact__line">m: 0417295031</p>
      <p class="contact__line">e: korva.holdings@mailbrook.example</p>
    </div>
  </section>

  <section class="card card--back">
    <div class="card__band">
      <div class="card__band-block"></div>
    </div>
    <div class="ghost-brand" aria-hidden="true">
      <span class="ghost-brand__name">korva</span>
      <span class="ghost-brand__legal">HOLDINGS PTY.LTD</span>
    </div>
    <div class="brand">
      <span class="brand__name">korva</span>
      <span class="brand__legal">KORVA HOLDINGS PTY.LTD</span>
      <span class="brand__services">Domestic / Residential / Commercial</span>
    </div>
    <div class="contact">
      <p class="contact__name">Marek Holtvay</p>
      <p class="contact__line">m: 0417295031</p>
      <p class="contact__line">e: korva.holdings@mailbrook.example</p>
    </div>
  </section>

</body>
</html>
```